Need a website setup for our new removalist business.
Our business is called Kettle Brook Removals and would like a website setup.
We don’t have a website, logo or design as of yet. Our truck is blue so something possibly that works and can incorporate the blue.

```html
<!DOCTYPE html>
<html lang="en">
<head>
<meta charset="utf-8">
<title>Kettle Brook Removals</title>
<link href="https://fonts.googleapis.com/css2?family=DM+Sans:ital,wght@0,400;0,500;0,700;0,800;1,400&display=swap" rel="stylesheet">
<style>
:root{
  --navy:#1c1851;
  --navy-2:#25216a;
  --red:#e3212b;
  --ink:#1c1b3a;
  --muted:#6d6f80;
  --pale:#f5f6fa;
  --white:#fff;
}
*{box-sizing:border-box;margin:0;padding:0}
html,body{width:1200px;height:3268px;overflow:hidden}
body{position:relative;font-family:'DM Sans',sans-serif;color:var(--ink);background:var(--white)}
.abs{position:absolute}
a{color:inherit;text-decoration:none}

.topbar{left:0;top:0;width:1200px;height:39px;background:var(--navy);color:#fff;font-size:11px;display:flex;align-items:center;padding:0 155px}
.topbar b{font-weight:700;margin-right:6px}
.topbar .arrow{color:var(--red);margin-right:6px}
.topbar .contact{margin-left:auto;display:flex;gap:22px;align-items:center}
.topbar .contact span i{color:var(--red);font-style:normal;margin-right:5px}
.topbar .social{display:flex;gap:10px;margin-left:12px;align-items:center}
.topbar .social svg{display:block}

.hero{left:0;top:39px;width:1200px;height:574px;background:linear-gradient(90deg,#2b3148 0%,#56688a 40%,#8aa0bd 70%,#b0bfd0 100%)}
.hero-shade{left:0;width:1200px;height:574px;background:linear-gradient(90deg,rgba(20,22,50,.75),rgba(20,22,50,.2) 60%,rgba(0,0,0,0))}
.header{left:155px;top:39px;width:1045px;height:78px;background:#fff;border-left:4px solid var(--red);display:flex;align-items:center;padding-left:30px}
.logo{display:flex;align-items:center;gap:10px;font-weight:800;font-size:19px;color:var(--navy);letter-spacing:.2px}
.logo .mark{width:22px;height:22px;background:var(--navy);display:block}
.nav{display:flex;gap:32px;margin-left:64px;font-size:11px;font-weight:500;color:var(--navy);text-transform:uppercase}
.nav .active{color:var(--red)}
.hero-tag{left:155px;top:373px;background:var(--red);color:#fff;font-size:9.5px;padding:8px 18px;text-transform:uppercase}
.hero-title{left:155px;top:410px;color:#fff;font-size:47px;font-weight:700;line-height:56px;width:760px}
.hero-sub{left:155px;top:532px;color:#fff;font-size:15px;font-style:italic}
.btn{display:flex;align-items:center;justify-content:center;font-size:11px;font-weight:700;text-transform:uppercase}
.btn-red{left:882px;top:464px;width:163px;height:34px;background:var(--red);color:#fff}
.btn-white{left:882px;top:512px;width:163px;height:36px;background:#fff;color:var(--navy);font-weight:500}

.about{left:155px;top:676px;width:890px;height:530px;background:var(--pale)}
.about-photo{left:186px;top:708px;width:367px;height:417px;background:linear-gradient(160deg,#6fa8c8,#a7c3d2 45%,#7b8590)}
.eyebrow{font-size:9px;font-weight:700;letter-spacing:.8px;color:#8a8c99;text-transform:uppercase;display:flex;align-items:center;gap:8px}
.eyebrow::before{content:"";width:14px;height:1px;background:#9a9cab}
.about-eyebrow{left:596px;top:724px}
.about-title{left:596px;top:742px;width:420px;font-size:29px;line-height:35px;font-weight:500;color:var(--navy)}
.about-text{left:596px;top:902px;width:420px;font-size:11px;line-height:19.5px;color:var(--muted)}
.checks{left:596px;top:972px;list-style:none;font-size:11px;color:var(--muted)}
.checks li{height:28px;display:flex;align-items:center;gap:8px}
.checks svg{flex:none}
.stats{left:596px;top:1069px;width:419px;height:107px;background:#fff;display:flex;align-items:center}
.stat{flex:1;text-align:center;border-right:1px solid #e8e9f0}
.stat:last-child{border-right:0}
.stat strong{display:block;font-size:28px;font-weight:500;color:var(--navy);line-height:32px}
.stat span{font-size:11px;color:var(--muted)}

.services{left:0;top:1272px;width:1200px;height:375px;background:#f6f7fb}
.services-eyebrow{left:0;top:1296px;width:1200px;justify-content:center}
.services-eyebrow::after{content:"";width:14px;height:1px;background:#9a9cab}
.services-title{left:0;top:1314px;width:1200px;text-align:center;font-size:29px;line-height:36px;font-weight:500;color:var(--navy)}
.card{background:#fff;height:219px;top:1405px}
.card-icon{position:absolute;right:0;top:0;width:59px;height:59px;background:var(--red);display:flex;align-items:center;justify-content:center}
.card h3{position:absolute;left:23px;top:70px;font-size:16px;font-weight:500;color:var(--navy)}
.card p{position:absolute;left:23px;top:102px;width:240px;font-size:11px;line-height:19.5px;color:var(--muted)}
.card .more{position:absolute;left:23px;top:176px;font-size:10px;font-weight:700;color:var(--navy);display:flex;align-items:center;gap:10px}
.card .more::before{content:"";width:16px;height:1px;background:var(--navy)}
.card-photo{left:459px;top:1405px;width:282px;height:219px;background:#fff}
.card-photo .img{position:absolute;left:0;top:0;width:282px;height:160px;background:linear-gradient(135deg,#9aa3ac,#d2c8b8 60%,#b0a697)}
.card-photo .icon{position:absolute;left:43px;top:160px;width:59px;height:59px;background:var(--red);display:flex;align-items:center;justify-content:center}
.card-photo h3{position:absolute;left:118px;top:180px;font-size:16px;font-weight:500;color:var(--navy)}

.quote-photo{left:0;top:1672px;width:1200px;height:448px;background:linear-gradient(90deg,#d6cfc8 0%,#4f6fb5 25%,#e7e5e4 45%,#c9c3bc 100%)}
.quote-box{left:600px;top:1742px;width:600px;height:449px;background:var(--navy)}
.quote-eyebrow{left:648px;top:1793px;color:#fff}
.quote-eyebrow::before{background:#fff}
.quote-title{left:648px;top:1810px;color:#fff;font-size:29px;font-weight:500}
.field{background:var(--navy-2);border:1px solid #34307a;color:#fff;font-size:11px;padding-left:11px;display:flex;align-items:center}
.field.msg{align-items:flex-start;padding-top:13px}
.submit{left:647px;top:2087px;width:398px;height:33px;background:var(--red);color:#fff}

.testi{left:0;top:2220px;width:1200px;height:482px;background:#f6f7fb}
.testi-photo{left:837px;top:2220px;width:363px;height:482px;background:linear-gradient(180deg,#e9e6e2,#cdb9a0 60%,#e4e0dc)}
.quote-mark{font-size:190px;font-weight:800;color:#e7e9f0;line-height:1}
.avatar{left:558px;top:2282px;width:84px;height:84px;border-radius:50%;background:linear-gradient(#c9a58f,#8b6c5c);border:3px solid #fff;box-shadow:0 0 0 1px #d8dae4}
.name-card{left:498px;top:2382px;width:204px;height:70px;background:#fff;text-align:center;padding-top:14px}
.name-card strong{display:block;font-size:14px;font-weight:500;color:var(--navy)}
.name-card span{font-size:9.5px;font-style:italic;color:var(--muted)}
.testi-text{left:360px;top:2490px;width:480px;text-align:center;font-size:15px;line-height:25px;font-style:italic;color:var(--navy)}
.dots{left:558px;top:2625px;display:flex;gap:6px;align-items:center}
.dots span{width:6px;height:6px;border-radius:50%;background:#d8dae4}
.dots .on{width:40px;height:2px;border-radius:0;background:var(--red)}

.band{left:0;top:2702px;width:1200px;height:226px;background:var(--navy);display:flex;padding:0 145px}
.band-col{flex:1;text-align:center;color:#fff;padding-top:42px;border-right:1px solid #2f2b70}
.band-col:last-child{border-right:0}
.band-col h4{color:var(--red);font-size:15px;font-weight:500;margin:14px 0 12px}
.band-col p{font-size:11.5px;line-height:20px}
.band-col a{display:block;margin-top:22px;font-size:10px;font-weight:700}

.footer{left:0;top:2928px;width:1200px;height:284px;background:#f6f7fb}
.f-logo{left:140px;top:2978px;font-size:15px;gap:8px}
.f-logo .mark{width:18px;height:18px}
.f-about{left:155px;top:3014px;width:210px;font-size:11px;line-height:19px;color:var(--muted)}
.f-est{left:155px;top:3126px;display:flex;gap:12px;align-items:center}
.f-est strong{display:block;font-size:15px;font-weight:500;color:var(--navy)}
.f-est span{font-size:11.5px;color:var(--red)}
.f-head{font-size:15px;font-weight:500;color:var(--navy)}
.f-head::after{content:"";display:block;width:16px;height:2px;background:var(--red);margin-top:8px}
.links{left:383px;top:3010px;list-style:none;font-size:11px;color:var(--muted)}
.links li{height:27.5px}
.links li::before{content:"✓ ";}
.post{display:flex;gap:12px;width:200px}
.post .thumb{width:55px;height:50px;flex:none;background:linear-gradient(135deg,#4b5a7a,#c5a27c)}
.post small{font-size:8.5px;color:var(--muted);display:block;margin-bottom:3px}
.post p{font-size:11px;line-height:16px;color:var(--navy)}
.f-news p{font-size:11px;line-height:19px;color:var(--muted);width:210px}
.subscribe{display:flex;margin-top:14px}
.subscribe span{width:167px;height:33px;background:#fff;border:1px solid #e1e3ea;font-size:9.5px;color:var(--muted);display:flex;align-items:center;padding-left:11px}
.subscribe b{width:39px;height:33px;background:var(--red);color:#fff;font-size:10px;display:flex;align-items:center;justify-content:center}
.f-social{display:flex;gap:9px;margin-top:17px}
.f-social span{width:26px;height:26px;border:1px solid var(--navy);border-radius:50%;display:flex;align-items:center;justify-content:center}
.bottom{left:0;top:3212px;width:1200px;height:56px;background:var(--navy);color:#fff;font-size:11px;text-align:center;padding-top:12px;line-height:17px}
.bottom i{color:var(--red);font-style:normal}
</style>
</head>
<body>

<div class="abs topbar">
  <b>TRACK ONLINE</b><span class="arrow">→</span>You can request status (pending confirmation) in 24 hours
  <div class="contact">
    <span><i>✉</i>info@kettlebrook.example</span>
    <span><i>▯</i>555 - 014-2298</span>
    <div class="social" aria-label="Social links">
      <svg width="10" height="10" viewBox="0 0 10 10"><circle cx="5" cy="5" r="4.2" fill="none" stroke="#fff"/><path d="M1 5h8M5 1c-2 2.5-2 5.5 0 8M5 1c2 2.5 2 5.5 0 8" fill="none" stroke="#fff" stroke-width=".8"/></svg>
      <svg width="10" height="10" viewBox="0 0 10 10"><path d="M1 1.5h8v5.5H4L2 9V7H1z" fill="#fff"/></svg>
      <svg width="10" height="10" viewBox="0 0 10 10"><circle cx="2" cy="5" r="1.5" fill="#fff"/><circle cx="8" cy="2" r="1.5" fill="#fff"/><circle cx="8" cy="8" r="1.5" fill="#fff"/><path d="M2 5l6-3M2 5l6 3" stroke="#fff"/></svg>
      <svg width="10" height="10" viewBox="0 0 10 10"><rect x="1" y="2" width="8" height="6" fill="none" stroke="#fff"/><path d="M1 2l4 3 4-3" fill="none" stroke="#fff"/></svg>
    </div>
  </div>
</div>

<div class="abs hero" role="img" aria-label="Photo of two warehouse staff checking a parcel with a tablet among shelving"></div>
<div class="abs hero-shade" style="top:39px"></div>

<header class="abs header">
  <div class="logo"><span class="mark"></span>Kettle Brook Removals</div>
  <nav class="nav">
    <a class="active">Home</a><a>About</a><a>Pages</a><a>Services</a><a>Portfolio</a><a>Blog</a><a>Contact</a>
  </nav>
</header>

<div class="abs hero-tag">Kettle Brook Removals</div>
<h1 class="abs hero-title">Friendly, Efficient and Reliable Service at Your Disposal.</h1>
<p class="abs hero-sub">Just sit back and let us worry about your move.</p>
<a class="abs btn btn-red">Request a callback</a>
<a class="abs btn btn-white">Contact us!</a>

<section class="abs about"></section>
<div class="abs about-photo" role="img" aria-label="Photo of a mover in a hard hat holding a clipboard"></div>
<div class="abs eyebrow about-eyebrow">About Transport</div>
<h2 class="abs about-title">No Residential Move Is Too Big Or Small For Our Experienced Moving Team At Kettle Brook Removals.</h2>
<p class="abs about-text">At our Kettle Brook depot, we fully appreciate how difficult it is for people to find reliable and trustworthy movers where they can store and ship their goods. We are always keen to prove to our customers that we are different!</p>
<ul class="abs checks">
  <li><svg width="10" height="10" viewBox="0 0 10 10"><path d="M1 5l3 3 5-7" fill="none" stroke="#e3212b" stroke-width="1.5"/></svg>Every Project is Run by a Team of Experts tempor incididunt.</li>
  <li><svg width="10" height="10" viewBox="0 0 10 10"><path d="M1 5l3 3 5-7" fill="none" stroke="#e3212b" stroke-width="1.5"/></svg>We Save Your Time, Money, and Space your modern home.</li>
  <li><svg width="10" height="10" viewBox="0 0 10 10"><path d="M1 5l3 3 5-7" fill="none" stroke="#e3212b" stroke-width="1.5"/></svg>Water features, streams and ponds in your garden.</li>
</ul>
<div class="abs stats">
  <div class="stat"><strong>50+</strong><span>Happy Clients</span></div>
  <div class="stat"><strong>80+</strong><span>Departments</span></div>
  <div class="stat"><strong>509+</strong><span>Expert Members</span></div>
</div>

<section class="abs services"></section>
<div class="abs eyebrow services-eyebrow">About Transport</div>
<h2 class="abs services-title">The Services That We Render Your<br>Indoor Transport</h2>

<article class="abs card" style="left:155px;width:281px">
  <div class="card-icon"><svg width="26" height="18" viewBox="0 0 26 18"><rect x="1" y="2" width="15" height="10" fill="#fff"/><path d="M17 5h5l3 4v3h-8z" fill="#fff"/><circle cx="6" cy="15" r="2.2" fill="#fff"/><circle cx="20" cy="15" r="2.2" fill="#fff"/></svg></div>
  <h3>Warehousing</h3>
  <p>At our Kettle Brook depot, we fully appreciate how difficult it is for people to find reliable and trustworthy storage!</p>
  <a class="more">READ MORE</a>
</article>
<article class="abs card-photo">
  <div class="img" role="img" aria-label="Photo of a mover with a pallet jack in a warehouse aisle"></div>
  <div class="icon"><svg width="26" height="18" viewBox="0 0 26 18"><rect x="1" y="2" width="15" height="10" fill="#fff"/><path d="M17 5h5l3 4v3h-8z" fill="#fff"/><circle cx="6" cy="15" r="2.2" fill="#fff"/><circle cx="20" cy="15" r="2.2" fill="#fff"/></svg></div>
  <h3>Transportation</h3>
</article>
<article class="abs card" style="left:765px;width:280px">
  <div class="card-icon"><svg width="26" height="18" viewBox="0 0 26 18"><path d="M1 9h24l-4 2H1zM10 9l5-7h3l-3 7zM10 11l5 6h3l-3-6zM2 9l-1-4h2l3 4z" fill="#fff"/></svg></div>
  <h3>Air Freight</h3>
  <p>At our Kettle Brook depot, we fully appreciate how difficult it is for people to find reliable and trustworthy shippers!</p>
  <a class="more">READ MORE</a>
</article>

<div class="abs quote-photo" role="img" aria-label="Photo of a smiling courier in a blue cap handing a box to a customer at a doorway"></div>
<section class="abs quote-box"></section>
<div class="abs eyebrow quote-eyebrow" style="color:#fff">Ready to help</div>
<h2 class="abs quote-title">Get A Free Quote Today.</h2>
<div class="abs field" style="left:647px;top:1865px;width:187px;height:37px">Your Name</div>
<div class="abs field" style="left:858px;top:1865px;width:187px;height:37px">Your Email</div>
<div class="abs field" style="left:647px;top:1925px;width:187px;height:37px">Phone Number</div>
<div class="abs field" style="left:858px;top:1925px;width:187px;height:37px">Subject</div>
<div class="abs field msg" style="left:647px;top:1986px;width:398px;height:76px">Message</div>
<a class="abs btn submit">Get an appointment!</a>

<section class="abs testi"></section>
<div class="abs quote-mark" style="left:55px;top:2330px">“</div>
<div class="abs quote-mark" style="left:228px;top:2440px">”</div>
<div class="abs testi-photo" role="img" aria-label="Photo of a young woman relaxing with a laptop among moving boxes"></div>
<div class="abs avatar" role="img" aria-label="Customer portrait"></div>
<div class="abs name-card"><strong>Maren Holt</strong><span>California</span></div>
<svg class="abs" style="left:592px;top:2452px" width="16" height="8" aria-hidden="true"><path d="M0 0h16l-8 8z" fill="#fff"/></svg>
<p class="abs testi-text">At our orthy garages where they can service and rice garage, we fully appreciate how difficult it is for people to fible and arages where they can service and repaire are always ke our customers that we are different!</p>
<div class="abs dots"><span></span><span></span><span class="on"></span><span></span></div>

<section class="abs band">
  <div class="band-col">
    <svg width="22" height="30" viewBox="0 0 22 30"><rect x="2" y="1" width="18" height="28" rx="2" fill="none" stroke="#fff" stroke-width="1.5"/><line x1="2" y1="6" x2="20" y2="6" stroke="#fff"/><line x1="2" y1="23" x2="20" y2="23" stroke="#fff"/></svg>
    <h4>Have a question? call us now</h4>
    <p>Office 1: +(03) 0155 210 7789<br>Office 2: +(03) 0155 210 7789</p>
    <a>CONTACT US</a>
  </div>
  <div class="band-col">
    <svg width="32" height="30" viewBox="0 0 32 30"><rect x="1" y="5" width="30" height="21" fill="none" stroke="#fff" stroke-width="1.5"/><path d="M1 5l15 12L31 5M1 26l11-10M31 26L20 16" fill="none" stroke="#fff" stroke-width="1.5"/></svg>
    <h4>Need support? Drop us an email</h4>
    <p>hello@kettlebrook.example<br>help@kettlebrook.example</p>
    <a>OUR FORM</a>
  </div>
  <div class="band-col">
    <svg width="28" height="30" viewBox="0 0 28 30"><circle cx="14" cy="17" r="11" fill="none" stroke="#fff" stroke-width="1.5"/><path d="M14 10v7l4 3M10 2h8" fill="none" stroke="#fff" stroke-width="1.5"/></svg>
    <h4>We are open on</h4>
    <p>Mon – Sat 06:00 – 20:00<br>Sunday – Closed</p>
    <a>READ MORE</a>
  </div>
</section>

<footer class="abs footer"></footer>
<div class="abs logo f-logo"><span class="mark"></span>Kettle Brook Removals</div>
<p class="abs f-about">We proide our selves on delivering on ises for main contractors in the South land, working on projects. loream Contary To Popular.</p>
<div class="abs f-est">
  <svg width="30" height="28" viewBox="0 0 30 28"><rect x="8" y="2" width="18" height="22" fill="none" stroke="#1c1851" stroke-width="1.6"/><rect x="2" y="8" width="14" height="18" fill="#f6f7fb" stroke="#1c1851" stroke-width="1.6"/></svg>
  <div><strong>Get Free Estimates</strong><span>+1800-555-019283</span></div>
</div>
<div class="abs f-head" style="left:383px;top:2974px">Quick Links</div>
<ul class="abs links">
  <li>About Us</li><li>Our Services</li><li>Real Time Tracking</li><li>Delivery Report</li><li>Supply Management</li><li>Contact Us</li>
</ul>
<div class="abs f-head" style="left:611px;top:2974px">Recent Posts</div>
<div class="abs post" style="left:611px;top:3017px"><div class="thumb" role="img" aria-label="Warehouse thumbnail"></div><div><small>▪ Nov 06, 2020</small><p>5 ways to boost the warehouse performanc...</p></div></div>
<div class="abs post" style="left:611px;top:3102px"><div class="thumb" role="img" aria-label="Truck at sunset thumbnail"></div><div><small>▪ Dec 24, 2020</small><p>We are the change in logistics : See insights...</p></div></div>
<div class="abs f-head" style="left:840px;top:2974px">Our Newsletter</div>
<div class="abs f-news" style="left:840px;top:3010px">
  <p>Subscribe to our newsletter to receive latest news on our services.</p>
  <div class="subscribe"><span>Email Address Here...</span><b>GO</b></div>
  <div class="f-social" aria-label="Social links">
    <span><svg width="12" height="12" viewBox="0 0 10 10"><circle cx="5" cy="5" r="4.2" fill="none" stroke="#1c1851"/><path d="M1 5h8M5 1c-2 2.5-2 5.5 0 8M5 1c2 2.5 2 5.5 0 8" fill="none" stroke="#1c1851" stroke-width=".8"/></svg></span>
    <span><svg width="12" height="12" viewBox="0 0 10 10"><path d="M1 1.5h8v5.5H4L2 9V7H1z" fill="#1c1851"/></svg></span>
    <span><svg width="12" height="12" viewBox="0 0 10 10"><circle cx="2" cy="5" r="1.5" fill="#1c1851"/><circle cx="8" cy="2" r="1.5" fill="#1c1851"/><circle cx="8" cy="8" r="1.5" fill="#1c1851"/><path d="M2 5l6-3M2 5l6 3" stroke="#1c1851"/></svg></span>
    <span><svg width="12" height="12" viewBox="0 0 10 10"><rect x="1" y="2" width="8" height="6" fill="none" stroke="#1c1851"/><path d="M1 2l4 3 4-3" fill="none" stroke="#1c1851"/></svg></span>
  </div>
</div>

<div class="abs bottom"><i>⚲</i> 12 Brookside Lane, Millbridge USA<br>Copyright © 2024</div>

</body>
</html>
```